Banner Ad to promote Youth Cycling Camps

We need a 728 x 90 banner ad to promote some youth cycling camps. There are 2 different camps - a road camp where they learn to ride their bikes on the roads and a mountain bike camp. The camps teach bike handling skills and racing tactics.

Target Market(s)

Parents of youth ages 7-17

Industry/Entity Type

Non-Profit

Font styles to use
Sans Serif

Requirements
Must have
• Logo
• Dates - Road Camp May 5-7, 2017
• - Mountain Bike Camp July 14-16, 2017
• website - quadrapedalcup.org
• be 728 x 90
Nice to have
• Animated - would like it to rotate with 3 slides - 1 a focus on both camps, 1 on road camp, 1 on mountain bike camp

```html
<!DOCTYPE html>
<html lang="en">
<head>
<meta charset="utf-8">
<title>Youth Cycling Camps – Banner Set</title>
<link href="https://fonts.googleapis.com/css2?family=Bowlby+One&family=Roboto+Condensed:wght@400;700;800&display=swap" rel="stylesheet">
<style>
  :root {
    --ink: #0d0d0d;
    --paper: #ffffff;
    --sun: #fff200;
    --sky: #7fd8ec;
    --white: #ffffff;
    --grey: #d9d9d9;
  }
  * { margin: 0; padding: 0; box-sizing: border-box; }
  html, body {
    width: 1200px;
    height: 639px;
    overflow: hidden;
    background: var(--paper);
  }
  .banner-set {
    position: relative;
    width: 1200px;
    height: 639px;
  }
  .banner {
    position: absolute;
    left: 43px;
    width: 1118px;
    height: 135px;
    display: block;
  }
  .banner--both { top: 38px; }
  .banner--road { top: 251px; }
  .banner--mtb { top: 462px; }

  .banner__bg { fill: var(--ink); }
  .logo__disc { fill: var(--sky); }
  .logo__name {
    font-family: "Roboto Condensed", sans-serif;
    font-weight: 800;
    font-size: 8.5px;
    fill: var(--ink);
    text-anchor: middle;
  }
  .headline {
    font-family: "Bowlby One", sans-serif;
    font-size: 17px;
    fill: var(--white);
    letter-spacing: 0.2px;
  }
  .camp {
    font-family: "Roboto Condensed", sans-serif;
    font-weight: 800;
    fill: var(--sun);
  }
  .date {
    font-family: "Roboto Condensed", sans-serif;
    font-weight: 800;
    fill: var(--white);
  }
  .ages__tab { fill: var(--sky); }
  .ages__text {
    font-family: "Roboto Condensed", sans-serif;
    font-weight: 700;
    font-size: 17px;
    fill: var(--ink);
    text-anchor: middle;
  }
  .web__tab { fill: var(--sun); }
  .web__text {
    font-family: "Roboto Condensed", sans-serif;
    font-weight: 800;
    font-size: 12.5px;
    letter-spacing: 0.8px;
    fill: var(--ink);
    text-anchor: middle;
  }
  .photo-edge { stroke: var(--sun); stroke-width: 1.2; fill: none; }
  .tagline {
    font-family: "Roboto Condensed", sans-serif;
    font-size: 7.6px;
    fill: var(--grey);
  }
  .tagline__lead { font-weight: 700; fill: var(--white); }
</style>
</head>
<body>
<main class="banner-set">

  <!-- Slide 1: both camps -->
  <svg class="banner banner--both" viewBox="0 0 727 88" preserveAspectRatio="none" aria-label="Both camps banner">
    <defs>
      <linearGradient id="photoBoth" x1="0" y1="0" x2="1" y2="1">
        <stop offset="0" stop-color="#5f7f9e"/>
        <stop offset="0.45" stop-color="#3d5f86"/>
        <stop offset="1" stop-color="#6f8f5a"/>
      </linearGradient>
    </defs>
    <rect class="banner__bg" width="727" height="88"/>
    <g role="img" aria-label="Photo of a large group of young riders with their bikes and a girl in a helmet riding a mountain bike">
      <polygon points="472,0 727,0 727,72 443,72" fill="url(#photoBoth)"/>
    </g>
    <polyline class="photo-edge" points="472,0 443,72"/>
    <circle class="logo__disc" cx="40" cy="44" r="32"/>
    <text class="logo__name" x="40" y="42">QUADRAPEDAL</text>
    <text class="logo__name" x="40" y="52">CUP</text>
    <text class="headline" x="80" y="22">BEST CYCLING CAMPS FOR YOUTH</text>
    <text class="camp" x="80" y="41" font-size="13">ROAD CAMP <tspan class="date">- MAY 5-7, 2017</tspan></text>
    <text class="camp" x="80" y="57" font-size="13">MOUNTAIN BIKE CAMP</text>
    <text class="date" x="80" y="76" font-size="13.5">JULY 14-16, 2017</text>
    <polygon class="ages__tab" points="330,29 458,29 446,58 318,58"/>
    <text class="ages__text" x="388" y="50">Ages 7-17</text>
    <polygon class="web__tab" points="290,66 449,66 440,88 281,88"/>
    <text class="web__text" x="363" y="82">quadrapedalcup.org</text>
    <text class="tagline" x="457" y="83"><tspan class="tagline__lead">PROFESSIONAL COACHES</tspan> Great Youth To Adult Ratio, Affordable</text>
  </svg>

  <!-- Slide 2: road camp -->
  <svg class="banner banner--road" viewBox="0 0 727 88" preserveAspectRatio="none" aria-label="Road camp banner">
    <defs>
      <linearGradient id="photoRoad" x1="0" y1="0" x2="1" y2="1">
        <stop offset="0" stop-color="#6f8a5e"/>
        <stop offset="0.5" stop-color="#8a9279"/>
        <stop offset="1" stop-color="#5e7550"/>
      </linearGradient>
    </defs>
    <rect class="banner__bg" width="727" height="88"/>
    <g role="img" aria-label="Photo of a pack of young road cyclists riding along a tree-lined road">
      <polygon points="472,0 727,0 727,72 443,72" fill="url(#photoRoad)"/>
    </g>
    <polyline class="photo-edge" points="472,0 443,72"/>
    <circle class="logo__disc" cx="40" cy="44" r="32"/>
    <text class="logo__name" x="40" y="42">QUADRAPEDAL</text>
    <text class="logo__name" x="40" y="52">CUP</text>
    <text class="headline" x="80" y="22">BEST CYCLING CAMPS FOR YOUTH</text>
    <text class="camp" x="80" y="53" font-size="27">ROAD CAMP</text>
    <text class="date" x="80" y="80" font-size="20">MAY 5-7, 2017</text>
    <polygon class="ages__tab" points="330,29 458,29 446,58 318,58"/>
    <text class="ages__text" x="388" y="50">Ages 7-17</text>
    <polygon class="web__tab" points="290,66 449,66 440,88 281,88"/>
    <text class="web__text" x="363" y="82">quadrapedalcup.org</text>
    <text class="tagline" x="457" y="83"><tspan class="tagline__lead">PROFESSIONAL COACHES</tspan> Great Youth To Adult Ratio, Affordable</text>
  </svg>

  <!-- Slide 3: mountain bike camp -->
  <svg class="banner banner--mtb" viewBox="0 0 727 88" preserveAspectRatio="none" aria-label="Mountain bike camp banner">
    <defs>
      <linearGradient id="photoMtb" x1="0" y1="0" x2="1" y2="1">
        <stop offset="0" stop-color="#7fa0b8"/>
        <stop offset="0.45" stop-color="#5d7f4c"/>
        <stop offset="1" stop-color="#8a9a63"/>
      </linearGradient>
    </defs>
    <rect class="banner__bg" width="727" height="88"/>
    <g role="img" aria-label="Photo of young mountain bikers riding a dirt trail by a lake among pine trees">
      <polygon points="472,0 727,0 727,72 443,72" fill="url(#photoMtb)"/>
    </g>
    <polyline class="photo-edge" points="472,0 443,72"/>
    <circle class="logo__disc" cx="40" cy="44" r="32"/>
    <text class="logo__name" x="40" y="42">QUADRAPEDAL</text>
    <text class="logo__name" x="40" y="52">CUP</text>
    <text class="headline" x="80" y="22">BEST CYCLING CAMPS FOR YOUTH</text>
    <text class="camp" x="80" y="52" font-size="17.5">MOUNTAIN BIKE CAMP</text>
    <text class="date" x="80" y="78" font-size="16.5">JULY 14-16, 2017</text>
    <polygon class="ages__tab" points="330,29 458,29 446,58 318,58"/>
    <text class="ages__text" x="388" y="50">Ages 7-17</text>
    <polygon class="web__tab" points="290,66 449,66 440,88 281,88"/>
    <text class="web__text" x="363" y="82">quadrapedalcup.org</text>
    <text class="tagline" x="457" y="83"><tspan class="tagline__lead">PROFESSIONAL COACHES</tspan> Great Youth To Adult Ratio, Affordable</text>
  </svg>

</main>
</body>
</html>
```